Website redesign for job agency recruitment

Please refer to the attached document, “Meridale Work Portal Outline,” for comprehensive details regarding the scope, objectives, and requirements of this website redesign project.

For imagery you can use images from this website https://www.pixaboreal.com or any other you regularly use.

Target Market(s)

Jobseekers and Companies looking for general labour

Industry/Entity Type

Services: Oil, Gas and Mining, Administrative, Construction and Trades, Warehouse and Logistics and, Manufacturing.

Number of Pages Required

5+ page

Font styles to use
Serif
Other font styles liked:
• Inter, Open-Sans or similar.

Requirements
Must have
• The requirements highlighted in the Word document attached. The final design needs to be provided in Figma including all viewports (Desktop, mobiel and tablet)
Should not have
• Website we like as a reference: www.quillvanestaffing.com, www.bexistaffing.com, www.zupran.com, www.fennickstaffing.com, www.7tpersonnel.com, www.hiringonthetrail.ca

```html
<!DOCTYPE html>
<html lang="en">
<head>
<meta charset="utf-8">
<title>Meridale Work Agency — Home</title>
<link href="https://fonts.googleapis.com/css2?family=Figtree:wght@400;500;600;700&display=swap" rel="stylesheet">
<style>
:root{
  --blue:#0d47a8;
  --blue-dark:#0a3a8c;
  --yellow:#f5b800;
  --ink:#2b2b2b;
  --muted:#4a4a4a;
  --grey:#efefef;
  --footer:#333333;
  --white:#ffffff;
}
*{box-sizing:border-box;margin:0;padding:0}
html,body{width:1200px;height:4053px;overflow:hidden;background:var(--white)}
body{position:relative;font-family:'Figtree',sans-serif;color:var(--ink)}
.abs{position:absolute}
a{color:inherit;text-decoration:none}

/* nav */
.nav{position:absolute;top:0;left:0;width:1200px;height:118px;background:var(--white)}
.nav-link{position:absolute;top:41px;font-size:18px;color:#333;transform:translateX(-50%);white-space:nowrap}
.nav-link.active{color:var(--blue);font-weight:600}
.nav-link.active::after{content:"";position:absolute;left:-22px;right:-22px;bottom:-12px;height:2px;background:var(--blue)}
.brand{position:absolute;left:598px;top:22px;transform:translateX(-50%);display:flex;align-items:center;gap:8px;font-size:15px;font-weight:700;color:var(--blue);white-space:nowrap}
.brand-dot{width:16px;height:16px;border-radius:50%;background:var(--yellow)}
.brand-tag{position:absolute;left:598px;top:84px;transform:translateX(-50%);font-size:9px;color:#777;white-space:nowrap}

/* hero */
.hero{position:absolute;top:118px;left:0;width:1200px;height:654px;
  background:linear-gradient(180deg,#000 0%,#0b1026 35%,#2a2f6e 62%,#7a4a7c 72%,#3a3f7a 82%,#1b1f3a 100%)}
.hero h1{position:absolute;top:110px;width:100%;text-align:center;color:var(--white);font-size:49px;font-weight:700;line-height:62px}
.hero h1 span{color:var(--yellow)}
.hero p{position:absolute;top:268px;width:100%;text-align:center;color:var(--white);font-size:19px}
.btn{position:absolute;height:50px;border-radius:25px;font-size:18px;display:flex;align-items:center;justify-content:center;color:var(--white)}
.btn-solid{background:var(--blue)}
.btn-ghost{border:1.5px solid rgba(255,255,255,.8)}

/* labels */
.eyebrow{position:absolute;font-size:18px;color:var(--blue);font-weight:500;letter-spacing:.3px}
.heading{position:absolute;font-size:37px;font-weight:600;color:var(--ink)}
.heading span{color:var(--blue)}
.center{width:1200px;left:0;text-align:center}

/* about */
.about-photo{position:absolute;left:113px;top:873px;width:445px;height:538px;border-radius:28px;border:2px solid #111;
  background:linear-gradient(135deg,#cfcac2,#e9e6e0 45%,#a89b8a)}
.about-text{position:absolute;left:598px;width:490px;font-size:15px;line-height:31.5px;color:var(--muted)}

/* services */
.svc-panel{position:absolute;left:879px;top:1633px;width:321px;height:483px;background:var(--grey)}
.svc-emblem{position:absolute;left:108px;top:1780px;width:276px;height:172px;border-radius:86px;
  background:linear-gradient(135deg,#fbeab0 0%,#f4f6fb 50%,#c9d6ee 100%)}
.svc-emblem-label{position:absolute;left:108px;top:1846px;width:276px;text-align:center;font-size:27px;font-weight:600;color:var(--blue)}
.svc-tab{position:absolute;left:193px;top:1702px;width:221px;height:44px;background:var(--blue);color:var(--white);border-radius:8px 8px 0 0;font-size:18px;font-weight:600;display:flex;align-items:center;justify-content:center}
.svc-item{position:absolute;font-size:18px;color:#333;display:flex;align-items:center;gap:14px;white-space:nowrap}
.arrow{color:var(--yellow);font-size:22px}
.svc-card{position:absolute;left:672px;top:1678px;width:267px;height:277px;background:var(--blue);border-radius:40px 8px 8px 8px;color:var(--white);padding:36px 28px;z-index:2}
.svc-card h3{font-size:18px;font-weight:600;margin-bottom:14px}
.svc-card p{font-size:14.5px;line-height:27px}
.svc-photo{position:absolute;left:824px;top:1811px;width:266px;height:264px;border-radius:24px;background:linear-gradient(160deg,#8fb6d6,#c7b59a 55%,#6f5a44)}

/* testimonials */
.testi-card{position:absolute;left:159px;top:2424px;width:884px;height:321px;background:var(--white);border-radius:28px;box-shadow:0 4px 18px rgba(0,0,0,.06)}
.avatar{position:absolute;left:267px;top:34px;width:82px;height:82px;border-radius:50%;background:linear-gradient(135deg,#8e7fb8,#c9c1dd)}
.quote-mark{position:absolute;left:188px;top:60px;color:var(--yellow);font-size:64px;font-weight:700;line-height:1}
.testi-name{position:absolute;left:366px;top:52px;font-size:18px;font-weight:600}
.testi-role{position:absolute;left:366px;top:84px;font-size:14px;color:var(--muted)}
.testi-quote{position:absolute;left:68px;top:150px;width:740px;border-left:3px solid var(--blue);padding-left:24px;font-size:14.5px;line-height:28px;color:var(--muted)}
.circle-btn{position:absolute;width:48px;height:48px;border:2px solid #333;border-radius:50%;display:flex;align-items:center;justify-content:center;font-size:24px}

/* why */
.why-card{position:absolute;top:3174px;width:299px;height:302px;border-radius:30px;background:var(--white);box-shadow:0 3px 16px rgba(0,0,0,.07);padding:42px 36px}
.why-card h3{font-size:18px;font-weight:600;line-height:23px;margin-bottom:24px}
.why-card p{font-size:14.5px;line-height:27.5px;color:var(--muted)}
.why-card.feature{background:var(--blue);color:var(--white);border-radius:40px 12px 12px 12px;border:2px solid #0a2f70}
.why-card.feature p{color:var(--white)}

/* footer */
.footer{position:absolute;left:0;top:3560px;width:1200px;height:493px}
.f-col{position:absolute;top:162px}
.f-col h4{color:var(--yellow);font-size:18px;font-weight:600;margin-bottom:16px}
.f-col li{list-style:none;color:var(--white);font-size:15px;line-height:32.6px}
.socials{display:flex;gap:10px;margin-top:14px}
.socials span{width:34px;height:34px;border-radius:50%;background:var(--yellow)}
.f-bar{position:absolute;left:0;bottom:0;width:1200px;height:45px;background:var(--blue);color:var(--white);font-size:13px;display:flex;align-items:center;justify-content:center}
</style>
</head>
<body>

<header class="nav">
  <a class="nav-link active" style="left:184px">Home</a>
  <a class="nav-link" style="left:304px">Candidates</a>
  <a class="nav-link" style="left:447px">Companies</a>
  <div class="brand"><span class="brand-dot"></span>Meridale Work Agency Ltd.</div>
  <div class="brand-tag">The right people to power your business</div>
  <a class="nav-link" style="left:749px">About Us</a>
  <a class="nav-link" style="left:868px">Contact</a>
  <a class="nav-link" style="left:1008px">Forms &amp; Links</a>
</header>

<section class="hero" role="img" aria-label="Highway at night with streaking light trails">
  <h1>The Right People. The Right Roles.<br>The Right <span>Results.</span></h1>
  <p>Connecting skilled professionals with leading employers across Canada’s most essential industries.</p>
  <a class="btn btn-solid" style="left:387px;top:322px;width:200px">For Candidates</a>
  <a class="btn btn-ghost" style="left:612px;top:322px;width:201px">For Employers</a>
</section>

<section>
  <div class="about-photo" role="img" aria-label="Team of professionals meeting around a table, seen from above"></div>
  <div class="eyebrow" style="left:599px;top:879px">ABOUT US</div>
  <h2 class="heading" style="left:599px;top:917px">About Meridale Work <span>Agency</span></h2>
  <p class="about-text" style="top:990px">Meridale Work Agency offers a complete range of staffing services to keep pace with your career or operational demands. We understand it’s not only daunting but very costly in both time and money to make your business thrive in a rapidly changing environment.</p>
  <p class="about-text" style="top:1138px">Our staffing and recruitment services are not just limited to finding good people. We are a Canada-wide team of capable search specialists, career counselors, HR specialists, and business consultants who enjoy providing our clients with a very customized staffing solution that evolves within their market. Each project provides a chance for us to apply our knowledge and shine.</p>
  <a class="btn btn-solid" style="left:598px;top:1359px;width:174px">Read More</a>
</section>

<section>
  <div class="eyebrow center" style="top:1546px">SERVICES</div>
  <h2 class="heading center" style="top:1574px">Our Core <span>Services</span></h2>
  <div class="svc-panel"></div>

  <div class="svc-emblem" role="img" aria-label="Decorative yellow and blue swoosh emblem"></div>
  <div class="svc-emblem-label">Our Services</div>

  <div class="svc-tab">Oil, Gas and Mining</div>
  <span class="arrow abs" style="left:428px;top:1708px">→</span>
  <div class="svc-item" style="left:384px;top:1789px">Administrative <span class="arrow">→</span></div>
  <div class="svc-item" style="left:421px;top:1866px">Warehouse &amp; Logistics <span class="arrow">→</span></div>
  <div class="svc-item" style="left:384px;top:1942px">Manufacturing <span class="arrow">→</span></div>
  <div class="svc-item" style="left:252px;top:2019px">Construction &amp; Trades <span class="arrow">→</span></div>

  <div class="svc-photo" role="img" aria-label="Drilling rig with stacked pipes on a worksite"></div>
  <div class="svc-card">
    <h3>Oil, Gas and Mining</h3>
    <p>Meridale Work Agency is a premiere Oil, Gas &amp; Mining staffing agency that can provide you with a reliable and experienced workforce. From rig hands to engineers,</p>
  </div>
</section>

<svg class="abs" style="left:0;top:2120px" width="1200" height="830" viewBox="0 0 1200 830" aria-hidden="true">
  <path d="M0 55 C200 40 380 -30 560 20 C720 60 850 140 1000 120 C1100 108 1160 90 1200 80 L1200 720 L0 720 Z" fill="var(--grey)"/>
  <path d="M860 115 C980 130 1100 110 1200 75 L1200 90 C1100 125 980 140 860 115 Z" fill="var(--blue)"/>
  <path d="M0 720 L0 690 C120 660 260 660 420 690 C560 720 620 810 760 810 C900 810 1000 760 1200 680 L1200 830 L0 830 Z" fill="var(--white)"/>
  <path d="M0 690 C120 660 260 655 420 685 C560 715 620 800 760 805 C650 815 560 760 420 720 C260 685 120 700 0 740 Z" fill="var(--blue)"/>
</svg>

<section>
  <div class="eyebrow center" style="top:2287px">TESTIMONIALS</div>
  <h2 class="heading center" style="top:2326px">What Our Clients <span>Say</span></h2>
  <div class="circle-btn" style="left:64px;top:2557px">←</div>
  <div class="circle-btn" style="left:1090px;top:2557px">→</div>
  <div class="testi-card">
    <div class="quote-mark">“</div>
    <div class="avatar" role="img" aria-label="Portrait of a client"></div>
    <div class="testi-name">— Operations Manager</div>
    <div class="testi-role">Oil &amp; Gas Company, Alberta</div>
    <p class="testi-quote">“Meridale Work consistently delivers skilled professionals who are ready to contribute from day one. Their responsiveness and understanding of our industry make them a trusted extension of our team.”Meridale Work consistently delivers skilled professionals who are ready to contribute from day one. Their responsiveness and understanding of our industry make them a trusted extension of our team.””</p>
  </div>
</section>

<section>
  <div class="eyebrow center" style="top:3028px">BUILT ON EXPERTISE. DRIVEN BY RESULTS.</div>
  <h2 class="heading center" style="top:3072px">Why Choose Meridale <span>Work</span></h2>
  <div class="why-card" style="left:113px">
    <h3>Rigorous Screening &amp;<br>Compliance</h3>
    <p>Every candidate undergoes a structured screening process to ensure skill verification, safety awareness, and cultural alignment. We prioritize reliability, qualifications, and workplace</p>
  </div>
  <div class="why-card feature" style="left:452px">
    <h3>Industry-Specific<br>Expertise</h3>
    <p>We specialize in Oil &amp; Gas, Mining, Construction, Manufacturing, Logistics, and Administrative staffing. Our team understands the demands, certifications, safety standards, and technical</p>
  </div>
  <div class="why-card" style="left:790px">
    <h3>Rapid Talent<br>Deployment</h3>
    <p>We move quickly without compromising quality. Our streamlined recruitment process allows us to deliver qualified professionals when and where you need them.</p>
  </div>
</section>

<footer class="footer">
  <svg class="abs" style="left:0;top:0" width="1200" height="493" viewBox="0 0 1200 493" aria-hidden="true">
    <path d="M0 120 C300 150 600 110 900 60 C1020 40 1120 30 1200 15 L1200 493 L0 493 Z" fill="var(--footer)"/>
    <path d="M0 110 C300 140 600 100 900 50 C1020 30 1120 15 1200 0 L1200 18 C1120 32 1020 44 900 64 C600 114 300 150 0 122 Z" fill="var(--yellow)"/>
  </svg>
  <div class="f-col" style="left:116px">
    <h4>Company Links</h4>
    <ul><li>Home</li><li>About Us</li><li>Candidates</li><li>Employers</li><li>Contact</li><li>Vancouver Location</li></ul>
  </div>
  <div class="f-col" style="left:368px;top:166px">
    <h4>Industries</h4>
    <ul><li>Oil, Gas &amp; Mining</li><li>Administrative</li><li>Construction &amp; Trades</li><li>Warehouse &amp; Logistics</li><li>Manufacturing</li></ul>
  </div>
  <div class="f-col" style="left:656px">
    <h4>Resources</h4>
    <ul><li>Terms of Use</li><li>Privacy Policy</li><li>Accessibility</li><li>Sitemap</li></ul>
  </div>
  <div class="f-col" style="left:882px;top:166px">
    <h4>Contact Info</h4>
    <ul><li>Vancouver, British Columbia</li><li>(604) 555-0142</li><li>info@meridalework.ca</li></ul>
    <div class="socials"><span></span><span></span><span></span></div>
  </div>
  <div class="f-bar">© 2026 Meridale Work Agency Ltd. All Rights Reserved.</div>
</footer>

</body>
</html>
```